Landing Page Design

This project needs landing page desing only. However, whoever wins this round will get to work directly on all other pages of the website as a separate private project.

See attached file for more details.

Target Market(s)

25-60 year old person who is looking for health insurance quotes.

Industry/Entity Type

Health Insurance

Number of Pages Required

1 page

Font styles to use
Sans Serif

Requirements
Must have
• see attachment
Nice to have
• see attachment
Should not have
• see attachment

```html
<!DOCTYPE html>
<html lang="en">
<head>
<meta charset="utf-8">
<title>CoverWiseQuotes.com – Compare Health Insurance Plans</title>
<link href="https://fonts.googleapis.com/css2?family=Roboto:wght@300;400;500;700;900&family=Roboto+Condensed:wght@400;700&display=swap" rel="stylesheet">
<style>
:root{
  --navy:#124a6a;
  --navy-dark:#0d3b57;
  --orange:#f15a22;
  --red:#e0412f;
  --sky:#cfe6f1;
  --sky-pale:#e4f1f7;
  --green:#3aa63a;
  --sun:#f8b45c;
  --violet:#a27cba;
  --violet-dark:#8b5fa6;
  --teal:#5cc0c3;
  --ink:#3d4a52;
  --muted:#7b8a93;
  --white:#ffffff;
}
*{box-sizing:border-box;margin:0;padding:0}
html,body{width:1200px;height:4569px;overflow:hidden;background:var(--white)}
body{font-family:"Roboto",Arial,sans-serif;color:var(--ink)}
.page{position:relative;width:1200px;height:4569px;overflow:hidden}
.abs{position:absolute}
.cond{font-family:"Roboto Condensed","Arial Narrow",sans-serif}

/* header */
.site-header{position:absolute;left:0;top:0;width:1200px;height:91px;background:var(--white)}
.brand{position:absolute;left:70px;top:24px;display:flex;align-items:center;gap:10px;font-weight:700;font-size:24px;color:var(--navy)}
.brand-mark{width:28px;height:28px;background:var(--navy)}
.call-pill{position:absolute;left:826px;top:8px;width:304px;height:72px;border-radius:36px;background:var(--orange);color:var(--white);display:flex;align-items:center;padding-left:16px;gap:14px}
.call-pill .circle{width:46px;height:46px;border-radius:50%;background:var(--white);display:flex;align-items:center;justify-content:center}
.call-pill small{display:block;font-size:14px;font-weight:700;letter-spacing:.5px}
.call-pill strong{display:block;font-size:27px;font-weight:700}

/* hero */
.hero{position:absolute;left:0;top:91px;width:1200px;height:695px;background:linear-gradient(120deg,#6b4a38 0%,#b88468 35%,#d9b08f 60%,#8c6a55 100%)}
.quote-box{position:absolute;left:536px;top:77px;width:609px;height:517px;background:rgba(255,255,255,.25)}
.quote-head{position:absolute;left:0;top:15px;width:609px;height:137px;background:var(--sky);text-align:center;color:var(--navy);font-weight:900;padding-top:22px}
.quote-head .l1{font-size:36px;line-height:42px}
.quote-head .l2{font-size:44px;line-height:50px}
.quote-sub{position:absolute;left:0;top:175px;width:609px;text-align:center;color:var(--white);font-weight:700;font-size:38px}
.zip-form{position:absolute;left:24px;top:280px;width:561px;height:62px;background:var(--white);border-radius:31px}
.zip-form span{position:absolute;left:28px;top:20px;font-size:18px;color:#9aa5ab}
.zip-btn{position:absolute;right:0;top:0;width:257px;height:62px;border-radius:31px;background:var(--green);color:var(--white);font-weight:700;font-size:20px;display:flex;align-items:center;justify-content:center;gap:18px}
.zip-btn i{width:42px;height:42px;border-radius:50%;background:var(--white);display:flex;align-items:center;justify-content:center}
.carriers{position:absolute;left:0;top:402px;width:609px;height:115px;background:var(--white);display:flex;align-items:center;justify-content:space-around;font-weight:700;font-size:22px;color:#6d7b84}

/* phone call */
.phone-cta{position:absolute;left:0;top:786px;width:1200px;height:250px;text-align:center}
.phone-cta .kicker{position:absolute;top:60px;width:100%;font-weight:700;font-size:20px;color:var(--navy)}
.phone-cta .kicker:before{content:"";display:inline-block;width:0;height:0;border-left:10px solid var(--orange);border-top:7px solid transparent;border-bottom:7px solid transparent;margin-right:8px}
.phone-cta .number{position:absolute;top:92px;width:100%;font-size:45px;color:var(--orange);font-weight:400}
.phone-cta .number b{font-weight:700}
.phone-cta .note{position:absolute;top:152px;width:100%;font-size:15px;color:var(--muted)}

/* states */
.states{position:absolute;left:0;top:1036px;width:1200px;height:700px}
.trust{position:absolute;top:30px;height:72px;border-radius:6px}
.state-panel{position:absolute;left:335px;top:115px;width:792px;height:585px;background:var(--navy)}
.state-list{position:absolute;font-size:14px;color:#d8e6ee;list-style:none}
.state-list li{height:27.7px}
.state-list li:before{content:"•";color:var(--orange);margin-right:8px}
.state-callout{position:absolute;left:76px;top:15px;width:335px;height:350px;background:var(--orange);border-radius:60px 0 0 0;color:var(--white);padding:52px 28px 0 38px}
.state-callout .small{font-size:17px;font-weight:500;letter-spacing:.3px}
.state-callout .big{margin-top:22px;font-weight:900;font-size:36px;line-height:40px}
.review{position:absolute;left:76px;width:260px;font-size:15px;color:#5a666d}
.review .bubble{background:#f1f3f4;border:1px solid #dde2e5;padding:14px 16px;line-height:20px}
.review .who{margin-top:14px;font-size:15px;color:var(--ink)}
.review .save{color:var(--green)}

/* plan types */
.plan-types{position:absolute;left:0;top:1822px;width:1200px;height:377px;background:var(--sun)}
.tab{position:absolute;color:var(--white);font-weight:700;font-size:26px;line-height:30px;padding:52px 0 0 36px;border-radius:70px 0 0 0}
.grid{position:absolute;border-collapse:collapse;font-size:14px;font-weight:700;color:var(--ink);background:var(--white);box-shadow:0 0 0 8px rgba(255,255,255,.35)}
.grid th{color:var(--white);font-size:15px;height:44px}
.grid td{height:44px;text-align:center;border-bottom:2px solid #f0e7dc}
.grid td:first-child{text-align:left;padding-left:16px}
.art{position:absolute}

/* tiers */
.plan-tiers{position:absolute;left:0;top:2199px;width:1200px;height:512px;background:var(--violet)}

/* guide */
.guide{position:absolute;left:0;top:2711px;width:1200px;height:975px}
.guide-title{position:absolute;top:150px;width:100%;text-align:center;color:var(--navy);font-weight:700}
.guide-title .t1{font-size:34px;line-height:38px;font-weight:400}
.guide-title .t2{font-size:40px;line-height:44px}
.card{position:absolute;width:330px}
.card-head{position:relative;height:86px;background:var(--sky-pale);padding:20px 10px 0 104px;font-weight:700;font-size:16px;line-height:20px;color:var(--navy)}
.card-icon{position:absolute;left:0;top:-4px;width:82px;height:104px}
.card p{margin-top:30px;font-size:15px;line-height:22px;color:var(--muted);height:90px;overflow:hidden}
.card .more{display:block;margin-top:18px;font-size:13px;font-weight:700;color:var(--navy)}

/* split */
.split{position:absolute;left:0;top:3686px;width:1200px;height:457px}
.split-left{position:absolute;left:0;top:0;width:600px;height:457px;background:var(--teal)}
.split-right{position:absolute;left:600px;top:0;width:600px;height:457px;background:var(--sun)}
.split h3{position:absolute;width:100%;text-align:center;color:var(--white);font-weight:700;font-size:24px;line-height:28px}
.or{position:absolute;left:578px;top:232px;width:44px;height:44px;border-radius:50%;background:var(--white);text-align:center;line-height:42px;font-size:16px;color:var(--muted)}

/* footer */
.site-footer{position:absolute;left:0;top:4143px;width:1200px;height:426px;background:var(--navy-dark);color:var(--white);text-align:center}
.footer-info{position:absolute;top:300px;font-size:15px;line-height:20px;text-align:left;display:flex;gap:14px}
.footer-info .ico{width:34px;height:34px;border-radius:50%;background:rgba(255,255,255,.15);flex:none;display:flex;align-items:center;justify-content:center}
.legal{position:absolute;left:0;top:396px;width:1200px;height:30px;background:#0a3049;font-size:13px;color:#9fb6c4}
</style>
</head>
<body>
<div class="page">

  <header class="site-header">
    <div class="brand"><span class="brand-mark"></span>CoverWiseQuotes.com</div>
    <div class="call-pill">
      <span class="circle"><svg width="24" height="24" viewBox="0 0 24 24"><path d="M6.6 10.8a15 15 0 0 0 6.6 6.6l2.2-2.2c.3-.3.7-.4 1-.2 1.1.4 2.3.6 3.6.6.6 0 1 .4 1 1V20c0 .6-.4 1-1 1A17 17 0 0 1 3 4c0-.6.4-1 1-1h3.5c.6 0 1 .4 1 1 0 1.3.2 2.5.6 3.6.1.3 0 .7-.2 1z" fill="#f15a22"/></svg></span>
      <div><small>CALL FOR QUOTES:</small><strong>(800) 555-0142</strong></div>
    </div>
  </header>

  <section class="hero" role="img" aria-label="Photo of a smiling family relaxing together at home">
    <div class="quote-box">
      <div class="quote-head"><div class="l1">COMPARE 2016</div><div class="l2">HEALTH INSURANCE PLANS</div></div>
      <div class="quote-sub">Get Your FREE Quotes Now!</div>
      <div class="zip-form"><span>Enter Zip Code</span>
        <div class="zip-btn">SEE PLANS <i><svg width="18" height="18" viewBox="0 0 18 18"><path d="M6 3l6 6-6 6" stroke="#3aa63a" stroke-width="3" fill="none"/></svg></i></div>
      </div>
      <div class="carriers"><span>Northvale</span><span>Crestline</span><span>Meridia</span><span>Harborview</span></div>
    </div>
  </section>

  <section class="phone-cta">
    <div class="kicker">TO SHOP OVER THE PHONE</div>
    <div class="number">CALL <b>1-800-555-0142</b></div>
    <div class="note">Speak with a licensed agent and get expert advice on choosing a plan that's right for you</div>
  </section>

  <section class="states">
    <div class="trust" style="left:786px;width:140px;background:#e7eaec"></div>
    <div class="trust" style="left:935px;width:186px;background:var(--navy)"></div>
    <div class="state-panel">
      <ul class="state-list" style="left:122px;top:50px"><li>Alabama</li><li>Alaska</li><li>Arizona</li><li>Arkansas</li><li>California</li><li>Colorado</li><li>Connecticut</li><li>Delaware</li><li>Florida</li><li>Georgia</li><li>Hawaii</li><li>Idaho</li><li>Illinois</li></ul>
      <ul class="state-list" style="left:289px;top:50px"><li>Indiana</li><li>Iowa</li><li>Kansas</li><li>Kentucky</li><li>Louisiana</li><li>Maine</li><li>Maryland</li><li>Massachusetts</li><li>Michigan</li><li>Minnesota</li><li>Mississippi</li><li>Missouri</li><li>Montana</li></ul>
      <ul class="state-list" style="left:442px;top:50px"><li>Nebraska</li><li>Nevada</li><li>New Hampshire</li><li>New Jersey</li><li>New Mexico</li><li>New York</li><li>North Carolina</li><li>North Dakota</li><li>Ohio</li><li>Oklahoma</li><li>Oregon</li><li>Pennsylvania</li><li>Rhode Island</li></ul>
      <ul class="state-list" style="left:625px;top:50px"><li>South Carolina</li><li>South Dakota</li><li>Tennessee</li><li>Texas</li><li>Utah</li><li>Vermont</li><li>Virginia</li><li>Washington</li><li>West Virginia</li><li>Wisconsin</li><li>Wyoming</li></ul>
      <svg class="abs" style="left:560px;top:440px" width="232" height="145" viewBox="0 0 232 145"><path d="M0 140 C80 130 170 95 232 10 L232 40 C180 110 100 145 0 145z" fill="#e0412f"/><path d="M20 120 C100 110 180 80 232 0 L232 8 C175 90 100 118 20 124z" fill="#ffffff"/></svg>
    </div>
    <div class="state-callout">
      <div class="small">CLICK YOUR STATE BELOW TO</div>
      <div class="big">GET FREE HEALTH INSURANCE QUOTES &amp; SAVE!</div>
    </div>
    <div class="review" style="top:380px"><div class="bubble">Very professional, knowledgeable, and friendly. Thanks for all your help!</div><div class="who">-Tom R., Tampa, FL</div></div>
    <div class="review" style="top:540px"><div class="bubble">Switched Plans and Saved Money!<br><span class="save">Annual Savings: $379.24</span></div><div class="who">-Anna K., Austin, TX</div></div>
  </section>

  <section class="plan-types">
    <div class="art" style="left:60px;top:150px;width:280px;height:170px;border-radius:30px;background:linear-gradient(135deg,#e0412f,#f07a4f)" role="img" aria-label="Illustration of a heart with a pulse line beside a medical clipboard"></div>
    <div class="tab" style="left:390px;top:36px;width:235px;height:213px;background:var(--red)">HEALTH<br>INSURANCE<br>PLAN TYPES</div>
    <table class="grid" style="left:618px;top:91px;width:509px">
      <tr style="background:var(--orange)"><th style="text-align:center;width:40%">PLAN TYPES</th><th>PPO</th><th>EPO</th><th>POS</th><th>HMO</th></tr>
      <tr><td>PCP Required?</td><td>NO</td><td>NO</td><td>YES</td><td>YES</td></tr>
      <tr><td>Referrals Required?</td><td>NO</td><td>NO</td><td>YES</td><td>YES</td></tr>
      <tr><td>Pre-Authorization Required?</td><td>YES</td><td>YES</td><td>NO</td><td>NO</td></tr>
      <tr><td>Out-of-Network Coverage?</td><td>YES</td><td>NO</td><td>YES</td><td>NO</td></tr>
    </table>
  </section>

  <section class="plan-tiers">
    <div class="tab" style="left:585px;top:116px;width:222px;height:228px;background:var(--violet-dark)">HEALTH<br>INSURANCE<br>PLAN TIERS</div>
    <table class="grid" style="left:76px;top:274px;width:512px">
      <tr style="background:var(--violet-dark)"><th>TIERS</th><th>BRONZE</th><th>SILVER</th><th>GOLD</th><th>PLATINUM</th></tr>
      <tr><td>COVERAGE LEVEL</td><td>60%</td><td>70%</td><td>80%</td><td>90%</td></tr>
      <tr><td>PREMIUM LEVEL</td><td>LOWEST</td><td>2nd LOWEST</td><td>2nd HIGHEST</td><td>HIGHEST</td></tr>
      <tr><td>DEDUCTIBLE</td><td>HIGHEST</td><td>MODERATE</td><td>NONE</td><td>NONE</td></tr>
      <tr><td>COST-SHARING</td><td>NONE</td><td>YES</td><td>NONE</td><td>NONE</td></tr>
    </table>
    <div class="art" style="left:840px;top:180px;width:250px;height:300px;border-radius:20px;background:linear-gradient(180deg,#c07a55,#e6e0ea,#f5c56a,#ffffff)" role="img" aria-label="Illustration of four stacked heart icons with a check mark for the plan tiers"></div>
  </section>

  <section class="guide">
    <div class="guide-title"><div class="t1">HOW DO</div><div class="t2">I BUY HEALTH INSURANCE?</div></div>

    <article class="card" style="left:76px;top:228px">
      <div class="card-head"><svg class="card-icon" viewBox="0 0 82 104"><path d="M0 0h82v80L41 104 0 80z" fill="#124a6a"/><path d="M41 66 24 49a10 10 0 0 1 17-11 10 10 0 0 1 17 11z" fill="#fff"/></svg>HOW DO I BUY HEALTH INSURANCE?</div>
      <p>For some, buying health insurance can be a confusing and overwhelming process. First, you have to find a health insurance plan within your budget...</p><span class="more">READ MORE</span>
    </article>
    <article class="card" style="left:436px;top:228px">
      <div class="card-head"><svg class="card-icon" viewBox="0 0 82 104"><path d="M0 0h82v80L41 104 0 80z" fill="#124a6a"/><path d="M22 62h38M26 60V46h6v14M38 60V36h6v24M50 60V28h6v32" stroke="#fff" stroke-width="3" fill="#fff"/></svg>WHAT IS THE HEALTHCARE MARKETPLACE?</div>
      <p>The passage of the Affordable Care Act established the Healthcare Marketplace. There are two distinct divisions - a state level, and a federal level. 37 states are members...</p><span class="more">READ MORE</span>
    </article>
    <article class="card" style="left:792px;top:228px">
      <div class="card-head"><svg class="card-icon" viewBox="0 0 82 104"><path d="M0 0h82v80L41 104 0 80z" fill="#124a6a"/><path d="M22 44h30l-6-6M60 56H30l6 6" stroke="#fff" stroke-width="4" fill="none"/></svg>WHAT'S THE "HEALTH INSURANCE EXCHANGE"?</div>
      <p>The Health Insurance Exchange is the pool of health care plans and providers which are cooperating with the federal government in order to provide affordable health insurance to...</p><span class="more">READ MORE</span>
    </article>
    <article class="card" style="left:76px;top:548px">
      <div class="card-head"><svg class="card-icon" viewBox="0 0 82 104"><path d="M0 0h82v80L41 104 0 80z" fill="#124a6a"/><rect x="24" y="28" width="30" height="36" fill="none" stroke="#fff" stroke-width="4"/><path d="M30 40h18M30 50h12" stroke="#fff" stroke-width="3"/></svg>WHEN CAN I SIGN UP FOR HEALTH INSURANCE?</div>
      <p>Keep the following terms in mind, as they will help make the search for insurance easier: Obamacare - a nickname (sometimes considered derogatory) for the Affordable...</p><span class="more">READ MORE</span>
    </article>
    <article class="card" style="left:436px;top:548px">
      <div class="card-head"><svg class="card-icon" viewBox="0 0 82 104"><path d="M0 0h82v80L41 104 0 80z" fill="#124a6a"/><rect x="26" y="26" width="30" height="40" fill="#fff"/><path d="M37 46h8M41 42v8" stroke="#124a6a" stroke-width="3"/></svg>HOW CAN I FIND THE BEST HEALTH INSURANCE COMPANY?</div>
      <p>Right now, there are hundreds of different health insurance companies participating in the Exchange offering thousands of different plans. These companies are rated on a letter...</p><span class="more">READ MORE</span>
    </article>
    <article class="card" style="left:792px;top:548px">
      <div class="card-head"><svg class="card-icon" viewBox="0 0 82 104"><path d="M0 0h82v80L41 104 0 80z" fill="#124a6a"/><path d="M26 62V38l10 10 10-16 10 10v20z" fill="#fff"/></svg>WHAT HAPPENS IF I STILL CAN'T AFFORD TO BUY HEALTH INSURANCE?</div>
      <p>If you cannot purchase insurance, the government will charge you a fee when you file your yearly income taxes. For 2016, the fine will be either $695 or 2% of your income...</p><span class="more">READ MORE</span>
    </article>
  </section>

  <section class="split">
    <div class="split-left">
      <svg class="abs" style="left:225px;top:-46px" width="150" height="260" viewBox="0 0 150 260"><path d="M0 0h150v190L75 250 0 190z" fill="#124a6a"/><path d="M0 185 75 240 150 185v20L75 260 0 205z" fill="#e0412f"/><rect x="35" y="70" width="36" height="48" fill="none" stroke="#fff" stroke-width="4"/><rect x="79" y="100" width="36" height="48" fill="none" stroke="#fff" stroke-width="4"/><path d="M50 140h20l-6-6M100 80H80l6 6" stroke="#fff" stroke-width="4" fill="none"/></svg>
      <h3 style="top:255px">COMPARE HEALTH INSURANCE<br>PLANS ONLINE</h3>
      <div class="abs" style="left:143px;top:330px;width:220px;height:50px;background:#fff;font-size:16px;color:#9aa5ab;padding:15px 18px">Enter Zip Code</div>
      <div class="abs" style="left:370px;top:330px;width:162px;height:50px;background:var(--red);color:#fff;font-weight:700;font-size:18px;text-align:center;line-height:50px">GET QUOTES</div>
    </div>
    <div class="split-right">
      <svg class="abs" style="left:225px;top:-46px" width="150" height="260" viewBox="0 0 150 260"><path d="M0 0h150v190L75 250 0 190z" fill="#124a6a"/><path d="M0 185 75 240 150 185v20L75 260 0 205z" fill="#e0412f"/><path d="M52 80c10 40 30 52 48 60l10-12-14-10-8 6c-8-6-14-14-18-22l6-8-8-16z" fill="#fff"/></svg>
      <h3 style="top:276px">SPEAK TO A<br>LICENSED AGENT</h3>
      <div class="abs" style="left:0;top:348px;width:600px;text-align:center;color:var(--red);font-weight:700;font-size:32px">1-800-555-0142</div>
      <div class="abs" style="left:0;top:400px;width:600px;text-align:center;color:#7a5a2a;font-size:13px">Mon-Fri, 8am-8pm EST</div>
    </div>
    <div class="or">or</div>
  </section>

  <footer class="site-footer">
    <div class="abs" style="left:0;top:50px;width:1200px;display:flex;justify-content:center;align-items:center;gap:10px;font-weight:700;font-size:24px"><span style="width:26px;height:26px;background:#fff;display:inline-block"></span>CoverWiseQuotes.com</div>
    <div class="abs" style="left:0;top:136px;width:1200px;font-weight:700;font-size:24px">CALL NOW TO GET YOUR FREE QUOTE COMPARISON</div>
    <div class="abs" style="left:0;top:180px;width:1200px;font-weight:700;font-size:34px;color:var(--sun)">(800) 555-0142</div>
    <div class="footer-info" style="left:185px"><span class="ico"><svg width="14" height="18" viewBox="0 0 14 18"><path d="M7 0a7 7 0 0 1 7 7c0 5-7 11-7 11S0 12 0 7a7 7 0 0 1 7-7z" fill="#fff"/><circle cx="7" cy="7" r="2.5" fill="#0d3b57"/></svg></span><div>120 Maple Ave<br>Suite 300, Fairview<br>OH 44100</div></div>
    <div class="footer-info" style="left:478px"><span class="ico"><svg width="16" height="16" viewBox="0 0 24 24"><path d="M6.6 10.8a15 15 0 0 0 6.6 6.6l2.2-2.2c.3-.3.7-.4 1-.2 1.1.4 2.3.6 3.6.6.6 0 1 .4 1 1V20c0 .6-.4 1-1 1A17 17 0 0 1 3 4c0-.6.4-1 1-1h3.5c.6 0 1 .4 1 1 0 1.3.2 2.5.6 3.6.1.3 0 .7-.2 1z" fill="#fff"/></svg></span><div>Phone<br>1-800-555-0142</div></div>
    <div class="footer-info" style="left:760px"><span class="ico"><svg width="16" height="12" viewBox="0 0 16 12"><rect width="16" height="12" fill="#fff"/><path d="M0 0l8 6 8-6" stroke="#0d3b57" stroke-width="1.5" fill="none"/></svg></span><div>Email<br>hello@coverwisequotes.com</div></div>
    <div class="legal">
      <span class="abs" style="left:140px;top:7px">Copyright © 2015 CoverWiseQuotes.com. All rights reserved</span>
      <span class="abs" style="left:615px;top:7px">Partners &nbsp;&nbsp; Privacy Policy &nbsp;&nbsp; Terms of Use</span>
      <span class="abs" style="left:880px;top:3px;width:24px;height:24px;border-radius:50%;border:2px solid #9fb6c4"></span>
      <span class="abs" style="left:912px;top:3px;width:24px;height:24px;border-radius:50%;border:2px solid #9fb6c4"></span>
    </div>
  </footer>

</div>
</body>
</html>
```